Trade Alert Service needs Youtube thumbnail / channel design

I'm about to set up a Youtube channel which gives real-time trade alerts to earn passive income. I'm looking for a Youtube channel design to include thumbnail and other associated visuals for the channel.
The trade alerts will be focused around selling cash-secured put options on US equities, and directed at people who want investing advice / tips for getting out of the rat race. I'd like the theme to be somewhat serious / credible, without too many eye-popping neon colours like all the other cheap trade alert videos / day trading videos on Youtube. Happy for you to use your experience if you think otherwise though, as you're the designer, not me!

Target Market(s)

Option Traders, Value Investors, People who want passive income

Industry/Entity Type

Finance

Logo Text

Bramblewick Quarter Guild

Requirements
Must have
• All relevant Youtube visuals so that I can upload them to the Youtube channel - all visuals required by Youtube Studio upload within the channel creation page.
A logo so that I can append it to Powerpoint presentations
Nice to have
• A blank Powerpoint slide template showing the logo would be great in chosen colour scheme

```html
<!DOCTYPE html>
<html lang="en">
<head>
<meta charset="utf-8">
<title>Bramblewick Quarter Guild — Thumbnail</title>
<link rel="stylesheet" href="https://fonts.googleapis.com/css2?family=Montserrat:wght@200;400;700&display=swap">
<style>
  :root {
    --sky: #3ccdf2;
    --aqua: #8ff0e6;
    --mint: #c9fbdf;
    --frame: #1b57c9;
    --pink: #f06bb0;
    --pink-soft: #f58bd6;
    --magenta: #d42b8d;
    --ghost: rgba(120, 200, 160, 0.22);
    --streak: rgba(255, 255, 255, 0.45);
    --photo-leaf: #5f9a3a;
    --photo-gold: #c9a646;
    --photo-skin: #d9b49a;
  }
  html, body {
    margin: 0;
    padding: 0;
    width: 1200px;
    height: 675px;
    overflow: hidden;
  }
  .thumbnail {
    position: relative;
    width: 1200px;
    height: 675px;
    overflow: hidden;
    font-family: "Montserrat", sans-serif;
    background: linear-gradient(20deg, var(--sky) 0%, var(--aqua) 45%, var(--mint) 80%);
  }
  .streaks {
    position: absolute;
    inset: 0;
  }
  .frame {
    position: absolute;
    left: 0; top: 0;
    width: 1200px; height: 675px;
    box-sizing: border-box;
    border-top: 5px solid var(--frame);
    border-left: 5px solid var(--frame);
    border-bottom: 5px solid var(--frame);
    -webkit-mask-image: linear-gradient(90deg, #000 55%, transparent 80%);
    mask-image: linear-gradient(90deg, #000 55%, transparent 80%);
  }
  .backdrop-word {
    position: absolute;
    left: 22px;
    top: -42px;
    margin: 0;
    font-weight: 200;
    font-size: 118px;
    letter-spacing: 1px;
    color: var(--ghost);
    white-space: nowrap;
  }
  .photo-plant {
    position: absolute;
    left: 724px;
    top: 0;
    width: 476px;
    height: 675px;
    background:
      radial-gradient(ellipse 90px 220px at 100px 230px, var(--photo-gold) 0%, rgba(201,166,70,0.6) 60%, transparent 100%),
      radial-gradient(ellipse 110px 160px at 90px 90px, var(--photo-leaf) 0%, transparent 100%),
      radial-gradient(ellipse 300px 130px at 260px 540px, var(--photo-skin) 0%, rgba(217,180,154,0.5) 60%, transparent 100%);
  }
  .title-block {
    position: absolute;
    left: 81px;
    top: 186px;
    width: 600px;
  }
  .kicker {
    position: absolute;
    left: 97px;
    top: 0;
    margin: 0;
    font-weight: 400;
    font-size: 38px;
    letter-spacing: 14px;
    color: var(--magenta);
    white-space: nowrap;
  }
  .headline {
    position: absolute;
    left: 0;
    top: 52px;
    margin: 0;
    font-weight: 700;
    font-size: 108px;
    line-height: 98px;
    color: var(--pink);
    background: linear-gradient(90deg, var(--pink), var(--pink-soft));
    -webkit-background-clip: text;
    background-clip: text;
    -webkit-text-fill-color: transparent;
  }
  .headline span { display: block; white-space: nowrap; }
  .headline .line-two { padding-left: 27px; }
  .tagline {
    position: absolute;
    left: 95px;
    top: 455px;
    margin: 0;
    font-weight: 400;
    font-size: 20px;
    line-height: 26px;
    letter-spacing: 7px;
    color: var(--magenta);
    text-align: center;
    white-space: nowrap;
  }
  .tagline span { display: block; }
  .brand-mark {
    position: absolute;
    right: 26px;
    top: 26px;
    display: flex;
    align-items: center;
    gap: 8px;
    font-weight: 700;
    font-size: 18px;
    color: var(--magenta);
  }
  .brand-mark .dot {
    width: 14px; height: 14px;
    background: var(--magenta);
  }
</style>
</head>
<body>
<main class="thumbnail">
  <svg class="streaks" width="1200" height="675" viewBox="0 0 1200 675" aria-hidden="true">
    <g stroke="var(--streak)" stroke-width="2" fill="none">
      <line x1="0" y1="70" x2="1200" y2="-200"/>
      <line x1="0" y1="200" x2="1200" y2="-80"/>
      <line x1="0" y1="345" x2="1200" y2="60"/>
      <line x1="0" y1="480" x2="1200" y2="190"/>
      <line x1="0" y1="620" x2="1200" y2="330"/>
      <line x1="0" y1="760" x2="1200" y2="470"/>
      <line x1="0" y1="900" x2="1200" y2="610"/>
    </g>
  </svg>
  <p class="backdrop-word">trading &amp; investing</p>
  <div class="frame"></div>

  <div class="photo-plant" role="img" aria-label="Hands holding soil with stacks of gold coins and young green plants growing from them"></div>

  <div class="title-block">
    <p class="kicker">BRAMBLEWICK</p>
    <h1 class="headline">
      <span class="line-one">QUARTER</span>
      <span class="line-two">GUILD</span>
    </h1>
  </div>

  <p class="tagline">
    <span>TRADING AND INVESTING</span>
    <span>OUR WAY TO FINANCIAL FREEDOM</span>
  </p>

  <div class="brand-mark">
    <span class="dot"></span>
    <span>Bramblewick</span>
  </div>
</main>
</body>
</html>
```